Design for a Note buying company that attracts landlords and seller financed notes

I need a card designed. I want a simple clean front with my logo and contact info. On the back I want some big and bold words to get a message across.

Our Company buys Notes (mortgages) and we want to convey the sense of financial security. Our number one market that we pursue is tired landlords.

If you want to understand our business you can visit our website. www.lakeviewpaperfund.com

Do not use any Clip Art in the design, it will not be accepted. I want a custom designed card not something I could throw together myself. Simple clean and drive the message home.

Target Market(s)

Landlords, seller financed note holders

Industry/Entity Type

Mortgage

Contact Information for Business Card

Simple clean and bold. I need to grab the attention of the customer. It should convey a professional touch.

Font styles to use
Sans Serif

Colors
ec2229
ffffff

Requirements
Must have
• Clean front with logo and contact information
Front colors should match logo

Back should be bold and grab attention. Back colors are open to ideas
Nice to have
• The Back May use the phrase "No more Tentants, No more Toilets" "More Time, More Cash"

I'm open to other ideas about grabbing a landlords attention

I'm open to a square card design
I like cards with round corners as well
Should not have
• any clip art! must be custom designs.

```html
<!DOCTYPE html>
<html lang="en">
<head>
<meta charset="utf-8">
<title>Lakeview Paper Fund – Business Card</title>
<link rel="stylesheet" href="https://fonts.googleapis.com/css2?family=Montserrat:wght@400;500;700;800&display=swap">
<style>
  :root {
    --brand-red: #ec2229;
    --white: #ffffff;
    --card-black: #262626;
    --card-edge: #1c1c1c;
    --stage: #161616;
    --muted: #d6d6d6;
  }
  * { box-sizing: border-box; margin: 0; padding: 0; }
  html, body {
    width: 1200px; height: 900px; overflow: hidden;
    background: var(--stage);
    font-family: "Montserrat", sans-serif;
    color: var(--white);
  }
  .canvas {
    position: relative; width: 1200px; height: 900px;
    display: flex; flex-direction: column; align-items: center; justify-content: center; gap: 48px;
  }
  .card {
    position: relative; width: 660px; height: 378px;
    background: linear-gradient(135deg, #2c2c2c 0%, var(--card-black) 55%, var(--card-edge) 100%);
    border-radius: 6px;
    box-shadow: 0 18px 40px rgba(0,0,0,.55);
  }
  /* Back side: brand name and message */
  .card-back {
    display: flex; flex-direction: column; align-items: center; justify-content: center;
  }
  .brand-name {
    font-weight: 800; font-size: 40px; letter-spacing: 3px; text-transform: uppercase;
    color: var(--muted); white-space: nowrap;
  }
  .brand-mark {
    display: inline-block; width: 14px; height: 14px; background: var(--brand-red);
    margin-right: 16px; vertical-align: middle; position: relative; top: -4px;
  }
  .message {
    margin-top: 48px; width: 100%;
    display: grid; grid-template-columns: 1fr auto 1fr; align-items: center; column-gap: 14px;
  }
  .message-rule { height: 3px; background: var(--brand-red); }
  .message-rule.left { align-self: end; margin-bottom: 14px; margin-left: 60px; }
  .message-rule.right { align-self: end; margin-bottom: 14px; margin-right: 60px; }
  .message-text {
    text-align: center; font-weight: 500; font-size: 21px; line-height: 1.3; letter-spacing: .5px;
    white-space: nowrap;
  }
  /* Front side: contact details */
  .card-front {
    display: flex; align-items: center; justify-content: center; padding: 0 40px;
  }
  .person { text-align: right; padding-right: 24px; white-space: nowrap; }
  .person-name {
    color: var(--brand-red); font-weight: 800; font-size: 30px; letter-spacing: 1.5px;
    text-transform: uppercase; line-height: 1.1;
  }
  .person-title { font-weight: 500; font-size: 20px; margin-top: 4px; }
  .divider { width: 2px; height: 128px; background: var(--brand-red); flex: none; }
  .contact { padding-left: 24px; font-size: 19px; font-weight: 500; line-height: 1.35; white-space: nowrap; }
  .contact-row { display: flex; align-items: center; gap: 8px; }
  .contact-row svg { width: 14px; height: 14px; flex: none; }
  .address { margin-bottom: 2px; padding-left: 22px; }
  .highlight { color: var(--brand-red); }
</style>
</head>
<body>
<main class="canvas">
  <section class="card card-back">
    <div class="brand-name"><span class="brand-mark"></span>Lakeview Paper Fund</div>
    <div class="message">
      <span class="message-rule left"></span>
      <p class="message-text">Skip the Repairs, Skip the Calls<br>Keep the Income, Gain Freedom</p>
      <span class="message-rule right"></span>
    </div>
  </section>

  <section class="card card-front">
    <div class="person">
      <h1 class="person-name">Dale Whitford</h1>
      <p class="person-title">Managing Director</p>
    </div>
    <span class="divider"></span>
    <div class="contact">
      <p class="address">P.O. Box 82<br>Millbrook, Kansas 67150</p>
      <p class="contact-row">
        <svg viewBox="0 0 16 16" aria-hidden="true"><path d="M4 1 L6.5 4 L5 6 C6 8.5 7.5 10 10 11 L12 9.5 L15 12 L13 15 C6.5 14 2 9.5 1 3 Z" fill="var(--brand-red)"/></svg>
        316-555-0142
      </p>
      <p class="contact-row">
        <svg viewBox="0 0 16 16" aria-hidden="true"><rect x="1.5" y="3.5" width="13" height="9" fill="none" stroke="var(--brand-red)" stroke-width="1.5"/><path d="M1.5 3.5 L8 9 L14.5 3.5" fill="none" stroke="var(--brand-red)" stroke-width="1.5"/></svg>
        info@lakeviewpaperfund.com
      </p>
      <p class="contact-row">
        <svg viewBox="0 0 16 16" aria-hidden="true"><circle cx="8" cy="8" r="6.5" fill="none" stroke="var(--brand-red)" stroke-width="1.4"/><ellipse cx="8" cy="8" rx="3" ry="6.5" fill="none" stroke="var(--brand-red)" stroke-width="1.2"/><path d="M1.5 8 H14.5" stroke="var(--brand-red)" stroke-width="1.2"/></svg>
        <span>www.<span class="highlight">lakeviewpaperfund</span>.com</span>
      </p>
    </div>
  </section>
</main>
</body>
</html>
```